Online tuition webpage design needed

Hi,
We are starting up an online tuition website for non- English speakers wishing to take an QRAVE test.

The webpage must include a place for people to enroll online in the course.
The home page must have:
• room for a logo (coming shortly, blue in colour)
• different packages of online tuition and coinvy
• tool bar showing different pages
• perhaps a video, small pictures

This is my site currently:-

www.lernmarowebtutor.example

as you can see, I am not very sure how to create a website … The large logo is what I would like to use, but I project has not been finalized yet. Please note, I don’t like the logo being that large!

Sites that are similar to what I am doing and like the design of are:

http://www.quorvapath.example.au/fees

https://www.brantiq9.example/index.php

http://www.tutorhalvekmorris.example.uk/index.html

http://www.vorplaneexam.example/

One thing I need is a place for student s to enroll, and if possible, I would like to use plovix to create exercises for students.
Currently, my site is using sitequill. My preference is to use plovix for online activities. I am not sure if I can use both.
Thanks in advance

Target Market(s)

people wising to take an QRAVE test (English proficiency test)

Industry/Entity Type

Online

Colors
3276b5
0292cd

Requirements
Must have
• a place for enrollment and admin login for students
plovix
video
talvo, gatherly, chirrup logos
Nice to have
• a booking calender
Should not have
• too much clutter. must be clean and professional looking

```html
<!DOCTYPE html>
<html lang="en">
<head>
<meta charset="utf-8">
<title>QRAVE Online Tuition</title>
<link href="https://fonts.googleapis.com/css2?family=Arimo:wght@400;700&display=swap" rel="stylesheet">
<style>
:root{
  --blue:#1d5fb0;
  --blue-dark:#0d3f95;
  --nav-top:#2f7ee0;
  --nav-bot:#1553c4;
  --text:#8a8a8a;
  --line:#dcdcdc;
  --cal:#4b87c6;
  --silver:#c8401c;
  --gold:#1d7d1d;
  --diamond:#0a2e9a;
  --footer:#4d4d4d;
  --white:#fff;
}
*{margin:0;padding:0;box-sizing:border-box}
html,body{width:843px;height:1200px;overflow:hidden;background:var(--white)}
body{position:relative;font-family:"Arimo",Arial,sans-serif;color:var(--text)}
.abs{position:absolute}
a{color:inherit;text-decoration:none}

.brand{left:100px;top:22px;display:flex;align-items:center;gap:8px}
.brand-mark{width:30px;height:30px;border-radius:50%;background:var(--blue)}
.brand-name{font-size:30px;color:var(--blue);line-height:1}
.brand-sub{left:152px;top:57px;font-size:12px;color:var(--blue)}
.top-links{right:100px;top:24px;font-size:8px;color:var(--blue-dark)}
.top-links span{margin:0 3px}
.search{left:618px;top:47px;width:125px;height:24px;border:1px solid #ccc;border-radius:3px;font-size:8px;padding:7px 6px;color:#999}
.search svg{position:absolute;right:7px;top:6px}

.nav{left:0;top:84px;width:843px;height:36px;background:linear-gradient(var(--nav-top),var(--nav-bot));color:var(--white);font-size:10.5px}
.nav a{position:absolute;top:13px}

.hero{left:99px;top:122px;width:646px;height:274px;background:linear-gradient(120deg,#c9c2b6,#8c5a3a 35%,#d2a080 55%,#6a3a26 80%,#b08a70)}
.hero-band{left:99px;top:358px;width:646px;height:38px;background:rgba(70,70,70,.55);color:var(--white);font-size:17.5px;padding:9px 27px;white-space:nowrap}
.dots{left:689px;top:373px;display:flex;gap:3px}
.dots i{width:10px;height:10px;border-radius:50%;background:#ccc}
.dots i:first-child{background:var(--blue-dark)}

h2{position:absolute;font-weight:400;color:var(--blue);font-size:16px}
.welcome-copy{left:99px;top:452px;width:390px;font-size:8.6px;line-height:16.4px;white-space:nowrap}
.btn-main{left:99px;top:553px;width:176px;height:31px;border-radius:3px;background:linear-gradient(#2a6fd6,var(--blue-dark));color:var(--white);font-size:10.5px;text-align:center;line-height:31px}
.video{left:501px;top:419px;width:240px;height:171px;background:linear-gradient(135deg,#f1ece2,#c89a72 45%,#6b4a3a 70%,#e8dccd)}
.video-bar{left:501px;top:564px;width:240px;height:26px;background:#1e1e1e}
.video-bar .track{position:absolute;left:4px;top:4px;width:232px;height:2px;background:#555}
.video-bar .track b{display:block;width:80px;height:2px;background:#2a8ce0}

.rule{left:99px;width:646px;height:1px;background:var(--line)}

.pkg{top:648px;width:114px;height:155px;border:1px solid #ccc;text-align:center}
.pkg-head{height:50px;color:var(--white);font-size:13px;line-height:42px;clip-path:polygon(0 0,100% 0,100% 62%,50% 100%,0 62%)}
.pkg-just{font-size:21px;font-weight:700;color:var(--blue);margin-top:2px}
.pkg-price{font-size:20px;font-weight:700;color:#333;margin-top:6px}
.pkg-btn{display:block;margin:13px auto 0;width:75px;height:23px;border:1px solid #bbb;border-radius:3px;font-size:9.5px;line-height:21px;color:var(--blue-dark)}

.cal-nav{left:720px;top:616px}
.cal-box{left:512px;top:644px;width:233px;height:174px;background:var(--cal);color:var(--white);font-size:9.5px}
.cal-box p{position:absolute;left:11px}
.cal-btn{left:522px;top:716px;width:109px;height:26px;border-radius:3px;background:var(--blue-dark);color:var(--white);font-size:8.5px;text-align:center;line-height:26px}
.cal-note{left:527px;top:755px;width:214px;font-size:8.2px;line-height:19px;color:var(--white);white-space:nowrap}
.mini{left:641px;top:643px;width:102px;height:99px;background:#f4f4f4;border:1px solid #bbb}
.mini-title{height:22px;margin-top:5px;background:#555;color:#ddd;font-size:8px;font-weight:700;text-align:center;line-height:22px}
.mini-days{display:grid;grid-template-columns:repeat(7,1fr);font-size:4.5px;text-align:center;color:#222;row-gap:6px;padding:6px 2px 0}
.mini-days .wk{color:var(--white);background:#4a5aa8}
.mini-days .mute{color:#aaa}

.svc-img{left:99px;width:119px;height:103px}
.svc-title{left:241px;font-size:11.5px;color:var(--blue)}
.svc-copy{left:241px;width:250px;font-size:8.2px;line-height:16.4px;white-space:nowrap}
.svc-copy a{color:var(--blue-dark);margin-left:18px}

.cats{left:512px;top:874px;width:233px;list-style:none}
.cats li{position:relative;height:30.8px;border-bottom:1px solid var(--line);font-size:8.6px;padding:10px 0 0 29px}
.cats li svg{position:absolute}
.cats .tick{left:7px;top:7px}
.cats .chev{right:5px;top:11px}

.footer{left:0;top:1118px;width:843px;height:82px;background:var(--footer);color:var(--white);font-size:8px}
.footer .links a{position:absolute;top:28px}
.copy{left:98px;top:48px}
.social{right:100px;top:19px;display:flex;gap:9px;font-size:8px;color:#eee;align-items:center}
.social span{display:flex;align-items:center;gap:3px}
.social i{width:9px;height:9px;border-radius:50%;border:1px solid #ccc;background:#777}
.cards{right:100px;top:60px;display:flex;gap:5px}
.cards span{width:22px;height:12px;background:var(--white);border-radius:1px;color:#333;font-size:5px;text-align:center;line-height:12px}
</style>
</head>
<body>

<header>
  <div class="abs brand"><span class="brand-mark"></span><span class="brand-name">QRAVE</span></div>
  <div class="abs brand-sub">Online Tuition</div>
  <div class="abs top-links"><a>Students Login</a><span>|</span><a>Enroll Here</a></div>
  <div class="abs search">Search
    <svg width="11" height="11" viewBox="0 0 11 11"><circle cx="4.5" cy="4.5" r="3.3" fill="none" stroke="#888" stroke-width="1.3"/><line x1="7" y1="7" x2="10.5" y2="10.5" stroke="#888" stroke-width="1.6"/></svg>
  </div>
  <nav class="abs nav">
    <a style="left:118px">Home</a><a style="left:182px">Tutorial Packages</a><a style="left:300px">Weekly Tips and Comments</a><a style="left:462px">Reading</a><a style="left:538px">Speaking</a><a style="left:617px">Listening</a><a style="left:694px">Writing</a>
  </nav>
</header>

<section>
  <div class="abs hero" role="img" aria-label="Photo of three smiling students looking at a laptop together"></div>
  <div class="abs hero-band">professional Help For people &nbsp; taking an Qrave</div>
  <div class="abs dots"><i></i><i></i><i></i></div>
</section>

<section>
  <h2 style="left:99px;top:418px">Welcome to QRAVE Online Tuition</h2>
  <p class="abs welcome-copy">All the Lorem Ipsum generators on the Internet tend to repeat predefined chunks as necessary,<br>making this the first true generator on the Internet. It uses a dictionary of over 200 Latin words,<br>combined with a handful of model sentence structures, to generate Lorem Ipsum which looks<br>reasonable. The generated Lorem Ipsum is therefore always free from repetition, injected<br>humour, or non-characteristic words</p>
  <a class="abs btn-main">View More Videos</a>
  <div class="abs video" role="img" aria-label="Video still of two students studying at a laptop in a kitchen"></div>
  <div class="abs video-bar">
    <div class="track"><b></b></div>
    <svg class="abs" style="left:90px;top:10px" width="140" height="10" viewBox="0 0 140 10" fill="#ddd">
      <polygon points="8,1 8,9 3,5"/><polygon points="18,1 24,5 18,9"/><polygon points="32,1 36,5 32,9"/><polygon points="36,1 40,5 36,9"/><rect x="48" y="2" width="6" height="6"/><polygon points="62,1 66,5 62,9"/><rect x="66" y="1" width="1.5" height="8"/>
      <rect x="90" y="4.5" width="34" height="1" fill="#888"/><circle cx="96" cy="5" r="2.5"/>
    </svg>
  </div>
</section>

<div class="abs rule" style="top:602px"></div>

<section>
  <h2 style="left:99px;top:613px">Our packages</h2>
  <div class="abs pkg" style="left:98px"><div class="pkg-head" style="background:var(--silver)">SILVER</div><div class="pkg-just">Just for</div><div class="pkg-price">$ 25.00</div><a class="pkg-btn">Sign up</a></div>
  <div class="abs pkg" style="left:230px"><div class="pkg-head" style="background:var(--gold)">GOLD</div><div class="pkg-just">Just for</div><div class="pkg-price">$ 35.00</div><a class="pkg-btn">Sign up</a></div>
  <div class="abs pkg" style="left:362px"><div class="pkg-head" style="background:var(--diamond)">DIAMOND</div><div class="pkg-just">Just for</div><div class="pkg-price">$ 45.00</div><a class="pkg-btn">Sign up</a></div>
</section>

<section>
  <h2 style="left:510px;top:613px">Calendar</h2>
  <svg class="abs cal-nav" width="22" height="14" viewBox="0 0 22 14" fill="none" stroke="var(--blue-dark)" stroke-width="2"><polyline points="7,2 2,7 7,12"/><polyline points="15,2 20,7 15,12"/></svg>
  <div class="abs cal-box">
    <p style="top:16px">Sunday 9-12</p>
    <p style="top:40px">Monday to Saturday 9-6</p>
  </div>
  <a class="abs cal-btn">Book an Application</a>
  <p class="abs cal-note">Lorem Ipsum, you need to be sure there isn't anything<br>embarrassing hidden in the middle of text.</p>
  <div class="abs mini">
    <div class="mini-title">SEPTEMBER 2013</div>
    <div class="mini-days">
      <span class="wk">SUN</span><span class="wk">MON</span><span class="wk">TUE</span><span class="wk">WED</span><span class="wk">THU</span><span class="wk">FRI</span><span class="wk">SAT</span>
      <span>1</span><span>2</span><span>3</span><span>4</span><span>5</span><span>6</span><span>7</span>
      <span>8</span><span>9</span><span>10</span><span>11</span><span>12</span><span>13</span><span>14</span>
      <span>15</span><span>16</span><span>17</span><span>18</span><span>19</span><span>20</span><span>21</span>
      <span>22</span><span>23</span><span>24</span><span>25</span><span>26</span><span>27</span><span>28</span>
      <span>29</span><span>30</span><span>31</span><span class="mute">1</span><span class="mute">2</span><span class="mute">3</span><span class="mute">4</span>
    </div>
  </div>
</section>

<div class="abs rule" style="top:836px"></div>

<section>
  <h2 style="left:100px;top:845px">Services</h2>
  <div class="abs svc-img" style="top:874px;background:linear-gradient(135deg,#d9c8c8,#6a5a7a 50%,#b7a3b8)" role="img" aria-label="Photo of two young girls with headphones at a laptop"></div>
  <div class="abs svc-title" style="top:876px">Streamed Classes</div>
  <p class="abs svc-copy" style="top:905px">Lorem Ipsum, you need to be sure there isn't anything embar-<br>rassing hidden in the middle of text. All the Lorem Ipsum<br>generators on the Internet tend to repeat predefined chunks<br>as necessary.... <a>More info</a></p>
  <div class="abs svc-img" style="top:1008px;height:102px;background:linear-gradient(135deg,#7a5a3a,#3a2a28 45%,#c89a5a)" role="img" aria-label="Photo of a teacher helping a young student at a desk"></div>
  <div class="abs svc-title" style="top:1010px">Practice Exams</div>
  <p class="abs svc-copy" style="top:1039px">Lorem Ipsum, you need to be sure there isn't anything embar-<br>rassing hidden in the middle of text. All the Lorem Ipsum<br>generators on the Internet tend to repeat predefined chunks<br>as necessary.... <a>More info</a></p>
</section>

<section>
  <h2 style="left:512px;top:845px">Categories</h2>
  <ul class="abs cats">
    <li><svg class="tick" width="10" height="11"><polyline points="1,6 4,10 9,1" fill="none" stroke="#999" stroke-width="1.3"/></svg>Business English<svg class="chev" width="6" height="10"><polyline points="1,1 5,5 1,9" fill="none" stroke="#888" stroke-width="1.3"/></svg></li>
    <li><svg class="tick" width="10" height="11"><polyline points="1,6 4,10 9,1" fill="none" stroke="#999" stroke-width="1.3"/></svg>Custom-made program<svg class="chev" width="6" height="10"><polyline points="1,1 5,5 1,9" fill="none" stroke="#888" stroke-width="1.3"/></svg></li>
    <li><svg class="tick" width="10" height="11"><polyline points="1,6 4,10 9,1" fill="none" stroke="#999" stroke-width="1.3"/></svg>Exam English<svg class="chev" width="6" height="10"><polyline points="1,1 5,5 1,9" fill="none" stroke="#888" stroke-width="1.3"/></svg></li>
    <li><svg class="tick" width="10" height="11"><polyline points="1,6 4,10 9,1" fill="none" stroke="#999" stroke-width="1.3"/></svg>Grammar<svg class="chev" width="6" height="10"><polyline points="1,1 5,5 1,9" fill="none" stroke="#888" stroke-width="1.3"/></svg></li>
    <li><svg class="tick" width="10" height="11"><polyline points="1,6 4,10 9,1" fill="none" stroke="#999" stroke-width="1.3"/></svg>Job interview preparation<svg class="chev" width="6" height="10"><polyline points="1,1 5,5 1,9" fill="none" stroke="#888" stroke-width="1.3"/></svg></li>
    <li><svg class="tick" width="10" height="11"><polyline points="1,6 4,10 9,1" fill="none" stroke="#999" stroke-width="1.3"/></svg>Skills based learning<svg class="chev" width="6" height="10"><polyline points="1,1 5,5 1,9" fill="none" stroke="#888" stroke-width="1.3"/></svg></li>
    <li><svg class="tick" width="10" height="11"><polyline points="1,6 4,10 9,1" fill="none" stroke="#999" stroke-width="1.3"/></svg>Vocabulary<svg class="chev" width="6" height="10"><polyline points="1,1 5,5 1,9" fill="none" stroke="#888" stroke-width="1.3"/></svg></li>
  </ul>
</section>

<footer class="abs footer">
  <div class="links">
    <a style="left:98px">Home</a><a style="left:138px">Tutorial Packages</a><a style="left:218px">Weekly Tips and Comments</a><a style="left:334px">Reading</a><a style="left:382px">Speaking</a><a style="left:432px">Listening</a><a style="left:481px">Writing</a>
  </div>
  <p class="abs copy">Copyright 2014 Qrave Online Tuition.All Right Reseved.</p>
  <div class="abs social"><span><i></i>chirrup</span><span><i></i>gatherly</span><span><i></i>plusora</span><span><i></i>talvo</span></div>
  <div class="abs cards"><span>coinvy</span><span>mintcard</span><span>vexa</span><span>amvero</span><span>dyscova</span></div>
</footer>

</body>
</html>
```